Delivery Performance Dashboard for Web Portal

We need you to design a dashboard for our web portal. We deliver sand and stone to construction jobsites. The attached screenshot is from our current web portal dashboard . It shows how much material has been delivered from an order.

Dump trucks will deliver multiple loads during the day and the dispatcher uses the dashboard to monitor if they need to add more trucks or less trucks to fulfill the order. An example would be, I need to ship 1,000 tons of sand to a jobsite and I plan to use 10 trucks during the day and that it will take 10 hours of hauling to complete the job. After 5 hours of hauling (50% the day is over), I should have delivered 500 tons of sand (50% of the order). But maybe there is a lot of traffic, and I only have delivered 300 tons. The dashboard will show that I am behind schedule and I might need to add 2 more trucks to the job.

Industry/Entity Type

Construction

Font styles to use
Sans Serif

Requirements
Must have
• We need a progress bar showing how much material has been delivered, how much material was requested to be delivered total and how much material should have been delivered at the current time. The goal is to show the user if the deliveries are ahead or behind the expected pace and why.
Nice to have
• The icons for plant, driving and jobsite show if the actual times have exceeded or beaten the planned times. Maybe you have other ideas to show the user if the trucks are sitting longer on the jobsite, at the plant to get loaded or driving to and from the jobsite.

```html
<!DOCTYPE html>
<html lang="en">
<head>
<meta charset="utf-8">
<title>Delivery Performance Dashboard</title>
<link rel="stylesheet" href="https://fonts.googleapis.com/css2?family=Poppins:wght@400;500;600&display=swap">
<style>
:root{
  --page:#eef2fb;
  --white:#ffffff;
  --ink:#2f3440;
  --muted:#6b7280;
  --purple:#6f6fcb;
  --bar-top-a:#7a6cd1;
  --bar-top-b:#4f8be6;
  --teal:#1cc0bd;
  --subhead:#d5e0f2;
  --line:#e4e7ee;
  --blue:#1e7ff0;
  --red:#dc3545;
  --orange:#fd7e14;
  --green:#28a745;
  --yellow:#ffc107;
  --cyan:#17a2b8;
  --grid:#dfe2e8;
}
*{box-sizing:border-box;margin:0;padding:0}
html,body{width:1200px;height:845px;overflow:hidden}
body{background:var(--page);font-family:'Poppins',sans-serif;color:var(--ink);position:relative}
.abs{position:absolute}

/* top bar */
.topbar{position:absolute;left:0;top:0;width:1200px;height:35px;background:linear-gradient(90deg,var(--bar-top-a),var(--bar-top-b));}
.brand{position:absolute;left:14px;top:7px;color:var(--white);font-weight:600;font-size:15px}
.search{position:absolute;left:910px;top:6px;width:139px;height:22px;background:var(--white);border-radius:2px;font-size:8px;color:#b4b8c2;padding:5px 0 0 22px}
.search svg{position:absolute;left:7px;top:6px}
.top-icon{position:absolute;top:9px}
.badge{position:absolute;left:1105px;top:9px;width:8px;height:8px;border-radius:50%;background:#ff6b6b;color:#fff;font-size:5px;text-align:center;line-height:8px}
.avatar{position:absolute;left:1129px;top:4px;width:28px;height:28px;border-radius:50%;background:radial-gradient(circle,#c98a5e,#6b4330);border:2px solid #fff}

.slogan{position:absolute;left:21px;top:60px;font-size:16px;font-weight:500;color:#383c45}

/* orders table */
.orders{position:absolute;left:12px;top:101px;width:575px;height:715px;background:var(--white)}
.orders table{width:100%;border-collapse:collapse;font-size:8.8px;color:#3a3f4a}
.orders th{background:var(--purple);color:#fff;font-weight:500;font-size:10.5px;text-align:left;height:44px;padding:0}
.orders td{height:55.9px;border-bottom:1px solid var(--line);padding:0}
.orders tr:last-child td{border-bottom:none}
.sort{display:inline-block;font-size:7px;line-height:6px;vertical-align:middle;margin-left:4px;text-align:center}
.c1{padding-left:8px!important;width:60px}
.c2{width:120px}.c3{width:134px}.c4{width:176px}

/* status panel */
.status{position:absolute;left:598px;top:101px;width:587px;height:432px;background:var(--white)}
.status-head{height:44px;background:var(--teal);color:#fff;font-size:10.5px;font-weight:500;padding:17px 0 0 17px}
.subhead{position:absolute;top:44px;height:31px;background:var(--subhead);font-size:9px;font-weight:500;color:#2d3340;padding:9px 0 0 13px}
.progress{position:absolute;left:13px;top:90px;width:280px;height:6px;border:1px solid #5a8fe0;border-radius:4px;overflow:hidden}
.progress span{display:block;width:59%;height:100%;background:linear-gradient(90deg,#7068cf,#5a8fe0)}
.t9{font-size:9px;color:#444a55}
.stat{font-size:8.6px;color:#6b7280}
.stat b{color:#3d434e;font-weight:500}
.split{position:absolute;height:5px;border-radius:3px;overflow:hidden;display:flex}
.split i{display:block;height:100%}
.legend{font-size:7.5px;color:#5b616c}
.legend i{display:inline-block;width:9px;height:9px;vertical-align:-1px;margin:0 6px 0 12px}
.chart{position:absolute;left:280px;top:190px}

/* cycle cards */
.card{position:absolute;width:287px;height:130px;background:var(--white)}
.card h3{position:absolute;left:13px;top:10px;font-size:11.5px;font-weight:500;color:#2d323c}
.card .avg{position:absolute;left:13px;top:30px;font-size:7.5px;color:#5d636e}
.card .close{position:absolute;right:11px;top:7px;font-size:9px;color:#555}
.card .kind{position:absolute;left:10px;top:53px;font-size:9.5px;color:#5b616c;display:flex;align-items:center;gap:6px}
.row-lbl{position:absolute;font-size:9px;color:#676d78}
.row-bar{position:absolute;height:5px;border-radius:3px}
.row-val{position:absolute;font-size:8.5px;color:#80858f}
</style>
</head>
<body>

<header class="topbar">
  <div class="brand">Your Logo</div>
  <div class="search"><svg width="9" height="9" viewBox="0 0 10 10"><circle cx="4" cy="4" r="3" fill="none" stroke="#777" stroke-width="1.3"/><path d="M6.3 6.3L9 9" stroke="#777" stroke-width="1.3"/></svg>Search...</div>
  <svg class="top-icon" style="left:1061px" width="14" height="14" viewBox="0 0 14 14"><path d="M1.5 1.5h11v8h-6l-3 3v-3h-2z" fill="none" stroke="#fff" stroke-width="1.3"/><path d="M4 5h6M4 7h4" stroke="#fff"/></svg>
  <svg class="top-icon" style="left:1093px" width="14" height="14" viewBox="0 0 14 14"><path d="M3 10V6a4 4 0 018 0v4l1 1H2z" fill="none" stroke="#fff" stroke-width="1.3"/><path d="M5.5 12.5h3" stroke="#fff" stroke-width="1.3"/></svg>
  <div class="badge">2</div>
  <div class="avatar" role="img" aria-label="User profile photo"></div>
  <svg class="top-icon" style="left:1169px;top:12px" width="13" height="11" viewBox="0 0 13 11"><path d="M1 1h11M4 4h8M1 7h11M4 10h8" stroke="#fff" stroke-width="1.3"/></svg>
</header>

<h1 class="slogan">Header Slogan Goes Here</h1>

<section class="orders">
  <table>
    <thead><tr>
      <th class="c1">Order<span class="sort">˄<br>˅</span></th>
      <th class="c2">Origin<span class="sort">˄<br>˅</span></th>
      <th class="c3" style="padding-left:48px">Destination<span class="sort">˄<br>˅</span></th>
      <th class="c4" style="padding-left:50px">Customer<span class="sort">˄<br>˅</span></th>
      <th style="padding-left:0">Status<span class="sort">˄<br>˅</span></th>
    </tr></thead>
    <tbody>
      <tr><td class="c1">177746</td><td>Ridgeview Asphalt Plant</td><td style="padding-left:3px">BZJV-185 from mm 77-98</td><td style="padding-left:8px">Hollins Paving - North Division</td><td style="padding-left:1px">Accepted</td></tr>
      <tr><td class="c1">177746</td><td>Ridgeview Asphalt Plant</td><td style="padding-left:3px">BZJV-185 from mm 77-98</td><td style="padding-left:8px">Hollins Paving - North Division</td><td style="padding-left:1px">Accepted</td></tr>
      <tr><td class="c1">177746</td><td>Ridgeview Asphalt Plant</td><td style="padding-left:3px">BZJV-185 from mm 77-98</td><td style="padding-left:8px">Hollins Paving - North Division</td><td style="padding-left:1px">Accepted</td></tr>
      <tr><td class="c1">177746</td><td>Ridgeview Asphalt Plant</td><td style="padding-left:3px">BZJV-185 from mm 77-98</td><td style="padding-left:8px">Hollins Paving - North Division</td><td style="padding-left:1px">Accepted</td></tr>
      <tr><td class="c1">177746</td><td>Ridgeview Asphalt Plant</td><td style="padding-left:3px">BZJV-185 from mm 77-98</td><td style="padding-left:8px">Hollins Paving - North Division</td><td style="padding-left:1px">Accepted</td></tr>
      <tr><td class="c1">177746</td><td>Ridgeview Asphalt Plant</td><td style="padding-left:3px">BZJV-185 from mm 77-98</td><td style="padding-left:8px">Hollins Paving - North Division</td><td style="padding-left:1px">Accepted</td></tr>
      <tr><td class="c1">177746</td><td>Ridgeview Asphalt Plant</td><td style="padding-left:3px">BZJV-185 from mm 77-98</td><td style="padding-left:8px">Hollins Paving - North Division</td><td style="padding-left:1px">Accepted</td></tr>
      <tr><td class="c1">177746</td><td>Ridgeview Asphalt Plant</td><td style="padding-left:3px">BZJV-185 from mm 77-98</td><td style="padding-left:8px">Hollins Paving - North Division</td><td style="padding-left:1px">Accepted</td></tr>
      <tr><td class="c1">177746</td><td>Ridgeview Asphalt Plant</td><td style="padding-left:3px">BZJV-185 from mm 77-98</td><td style="padding-left:8px">Hollins Paving - North Division</td><td style="padding-left:1px">Accepted</td></tr>
      <tr><td class="c1">177746</td><td>Ridgeview Asphalt Plant</td><td style="padding-left:3px">BZJV-185 from mm 77-98</td><td style="padding-left:8px">Hollins Paving - North Division</td><td style="padding-left:1px">Accepted</td></tr>
      <tr><td class="c1">177746</td><td>Ridgeview Asphalt Plant</td><td style="padding-left:3px">BZJV-185 from mm 77-98</td><td style="padding-left:8px">Hollins Paving - North Division</td><td style="padding-left:1px">Accepted</td></tr>
      <tr><td class="c1">177746</td><td>Ridgeview Asphalt Plant</td><td style="padding-left:3px">BZJV-185 from mm 77-98</td><td style="padding-left:8px">Hollins Paving - North Division</td><td style="padding-left:1px">Accepted</td></tr>
    </tbody>
  </table>
</section>

<section class="status">
  <div class="status-head">Current Status - Loading/Delivery Report</div>
  <div class="subhead" style="left:0;width:303px">Tons<span class="sort" style="margin-left:10px">˄<br>˅</span></div>
  <div class="subhead" style="left:306px;width:125px;padding-left:16px">Wait Times<span class="sort" style="margin-left:10px">˄<br>˅</span></div>
  <div class="subhead" style="left:433px;width:84px">Remaining</div>
  <div class="subhead" style="left:519px;width:68px;padding-left:16px;color:var(--blue)">+/-
    <svg width="12" height="8" viewBox="0 0 12 8" style="vertical-align:-1px"><rect x="0" y="0" width="7" height="6" fill="#222"/><path d="M7 2h3l2 2v2H7z" fill="#222"/><circle cx="2.5" cy="7" r="1" fill="#222"/><circle cx="9.5" cy="7" r="1" fill="#222"/></svg></div>

  <div class="progress"><span></span></div>
  <div class="abs t9" style="left:16px;top:104px">722.57 / 1500</div>
  <div class="abs t9" style="left:201px;top:104px">7:30 am - 5:00 pm</div>

  <svg class="abs" style="left:320px;top:91px" width="70" height="8" viewBox="0 0 70 8">
    <path d="M0 8V1l3 2V1l3 2V1l2 0v7z" fill="#888"/><path d="M11 6l2-3 2 3z" fill="var(--red)"/>
    <rect x="22" y="1" width="6" height="5" fill="#888"/><path d="M28 3h2l1 2v1h-3z" fill="#888"/><path d="M33 6l2-3 2 3z" fill="var(--red)"/>
    <path d="M46 8c-2-3-3-4-3-5a3 3 0 016 0c0 1-1 2-3 5z" fill="#888"/><path d="M53 3l2 3 2-3z" fill="var(--green)"/>
  </svg>
  <div class="abs" style="left:478px;top:91px;font-size:8.5px;color:var(--green)">+1:25 hrs</div>
  <div class="abs" style="left:540px;top:91px;font-size:8.5px;color:var(--red)">-31</div>

  <div class="abs legend" style="left:370px;top:161px"><i style="background:var(--green)"></i>Esitmated Schedule<i style="background:var(--red)"></i>Current Schedule</div>

  <div class="abs stat" style="left:18px;top:170px">Scheduled Load: <b>1500 ton</b></div>
  <div class="abs stat" style="left:18px;top:189px">Esitamated Time: <b>3 hrs 25 mins</b></div>
  <div class="abs stat" style="left:18px;top:223px">Materials Delivered</div>
  <div class="split" style="left:19px;top:243px;width:191px"><i style="width:38%;background:var(--blue)"></i><i style="flex:1;background:var(--red)"></i></div>
  <div class="abs stat" style="left:26px;top:252px"><b>800</b></div>
  <div class="abs stat" style="left:114px;top:252px"><b>700</b></div>
  <div class="abs stat" style="left:19px;top:288px">Time Taken</div>
  <div class="split" style="left:20px;top:308px;width:189px"><i style="width:48%;background:var(--orange)"></i><i style="flex:1;background:var(--red)"></i></div>
  <div class="abs stat" style="left:22px;top:318px"><b>2 hrs 35 mins</b></div>
  <div class="abs stat" style="left:99px;top:318px"><b>1 hrs 10 mins</b></div>
  <div class="abs stat" style="left:20px;top:349px">Ahead/Behind Schedule : <b style="color:var(--red);font-size:9px">&nbsp;45 mins</b>
    <svg width="8" height="9" viewBox="0 0 8 9" style="margin-left:4px;vertical-align:-1px"><path d="M4 0v8M1 5l3 3 3-3" fill="none" stroke="var(--red)" stroke-width="1.3"/></svg></div>
  <div class="abs stat" style="left:19px;top:374px">To Meet Schedule Need More Trucks : <b style="color:var(--red)">&nbsp;3</b></div>

  <svg class="chart" width="307" height="215" viewBox="0 0 307 215" font-family="Poppins, sans-serif" font-size="8.8" fill="#555">
    <g stroke="var(--grid)" stroke-width="1">
      <line x1="41" y1="13" x2="288" y2="13"/>
      <line x1="41" y1="50" x2="288" y2="50"/>
      <line x1="41" y1="85" x2="288" y2="85"/>
      <line x1="41" y1="121" x2="288" y2="121"/>
      <line x1="41" y1="157" x2="288" y2="157"/>
      <line x1="41" y1="187" x2="288" y2="187"/>
    </g>
    <g text-anchor="end">
      <text x="34" y="17">5 hr</text>
      <text x="34" y="54">4 hr</text>
      <text x="34" y="89">3 hr</text>
      <text x="34" y="122">2 hr</text>
      <text x="33" y="161">1 hr</text>
    </g>
    <line x1="41" y1="187" x2="180" y2="68" stroke="var(--green)" stroke-width="1.6"/>
    <line x1="41" y1="187" x2="188" y2="106" stroke="var(--red)" stroke-width="1.6"/>
    <g text-anchor="middle">
      <text x="46" y="206">0</text>
      <text x="99" y="206">500</text>
      <text x="151" y="206">1000</text>
      <text x="208" y="206">1500</text>
      <text x="279" y="206">2000</text>
    </g>
  </svg>
</section>

<article class="card" style="left:598px;top:545px">
  <h3>Order 17746</h3><div class="avg">Avg Cycle Time : 2 hrs 27 min</div><div class="close">✕</div>
  <div class="kind"><svg width="16" height="12" viewBox="0 0 16 12"><path d="M0 12V1l5 3V1l5 3V1h6v11z" fill="#888"/></svg>Plant (min)</div>
  <div class="row-lbl" style="left:9px;top:76px">Planned</div><div class="row-bar" style="left:52px;top:79px;width:176px;background:var(--blue)"></div><div class="row-val" style="left:235px;top:74px">30</div>
  <div class="row-lbl" style="left:17px;top:95px">Actual</div><div class="row-bar" style="left:52px;top:98px;width:210px;background:var(--red)"></div><div class="row-val" style="left:265px;top:95px">33</div>
</article>

<article class="card" style="left:898px;top:545px">
  <h3>Order 17746</h3><div class="avg">Avg Cycle Time : 2 hrs 27 min</div><div class="close">✕</div>
  <div class="kind"><svg width="18" height="13" viewBox="0 0 18 13"><rect x="0" y="0" width="11" height="9" fill="#888"/><path d="M11 3h4l3 3v3h-7z" fill="#888"/><circle cx="4" cy="11" r="2" fill="#888"/><circle cx="14" cy="11" r="2" fill="#888"/></svg>Diving (min)</div>
  <div class="row-lbl" style="left:9px;top:76px">Planned</div><div class="row-bar" style="left:52px;top:79px;width:156px;background:var(--yellow)"></div><div class="row-val" style="left:215px;top:74px">60</div>
  <div class="row-lbl" style="left:17px;top:95px">Actual</div><div class="row-bar" style="left:52px;top:98px;width:204px;background:var(--red)"></div><div class="row-val" style="left:265px;top:95px">83</div>
</article>

<article class="card" style="left:598px;top:686px">
  <h3>Order 17746</h3><div class="avg">Avg Cycle Time : 2 hrs 27 min</div><div class="close">✕</div>
  <div class="kind"><svg width="12" height="15" viewBox="0 0 12 15"><path d="M6 15C2 9 0 7 0 5a6 6 0 0112 0c0 2-2 4-6 10z" fill="#888"/><circle cx="6" cy="5" r="2" fill="#fff"/></svg>Jobsite (min)</div>
  <div class="row-lbl" style="left:9px;top:76px">Planned</div><div class="row-bar" style="left:52px;top:79px;width:194px;background:var(--green)"></div><div class="row-val" style="left:253px;top:74px">30</div>
  <div class="row-lbl" style="left:17px;top:95px">Actual</div><div class="row-bar" style="left:52px;top:98px;width:194px;background:var(--green)"></div><div class="row-val" style="left:253px;top:95px">30</div>
</article>

<article class="card" style="left:898px;top:686px">
  <h3>Order 17746</h3><div class="avg">Avg Cycle Time : 2 hrs 27 min</div><div class="close">✕</div>
  <div class="kind"><svg width="14" height="14" viewBox="0 0 14 14"><circle cx="7" cy="7" r="4.5" fill="none" stroke="#888" stroke-width="3" stroke-dasharray="2.4 1.2"/><circle cx="7" cy="7" r="3.5" fill="#888"/><circle cx="7" cy="7" r="1.5" fill="#fff"/></svg>Equipment (min)</div>
  <div class="row-lbl" style="left:9px;top:76px">Planned</div><div class="row-bar" style="left:52px;top:79px;width:156px;background:var(--cyan)"></div><div class="row-val" style="left:215px;top:74px">60</div>
  <div class="row-lbl" style="left:17px;top:95px">Actual</div><div class="row-bar" style="left:52px;top:98px;width:204px;background:var(--red)"></div><div class="row-val" style="left:260px;top:95px">83</div>
</article>

</body>
</html>
```